3 x Professional Herbal Supplement Label Design Ready to Print in UK Standard + Example inc

Hi,
Thank you for taking the time to read. I'm looking for an excellent graphic designer experienced in creating supplement labels for our 3 new products. The labels should be sized and have the resolution ready for the printers.
Here is the work:
I'm looking for a new supplement label design that I can use for 3 new products called:
1 - Raspberry Ketone
2 - Garcinia Cambogia
3 - Green Coffee
You will only need to create a single label to enter the competition, as the label created will be the template for all 3 products listed above. You can choose whether you go for product 1, 2,or 3 to enter the design competition, but all 3 will be required on completion should you be selected.
Simply, the label template would be adjusted for the other products, what would be different is the product specifics like, name, background graphic of the ingredient and ingredients listed, directions of use, barcode etc.
The design I like, which I'd like you to copy and then artistically make different is attached and titled "BrightMeadow_Garcinia_Cambogia_LABEL.jpg"
My company logo is attached called "vorix final logo.ai" & "vorix-invis.png" - Please let me know if this resolution is not suitable.
The guidance information in designing a UK label from the supplement manufacturer is attached, as follows:
The supplement manufacturer has also provided a very basic example of a product they produced for another company (Not very good I know, but at least shows what goes where). Please do not use this as an example of a good design!
*** I will provide more specific product detail (ingredients, bar-code, dosage) if your initial design is liked and selected for adjustment, as we will require that all 3 label designs are completed.
*** The delivered image files will need to be in Photoshop format.

```html
<!DOCTYPE html>
<html lang="en">
<head>
<meta charset="utf-8">
<title>vorix Raspberry Ketone Label</title>
<link rel="stylesheet" href="https://fonts.googleapis.com/css2?family=Roboto+Condensed:wght@400;700;900&display=swap">
<style>
  :root {
    --pink: #e8336b;
    --pink-deep: #d81f5a;
    --pink-soft: #f59bb8;
    --pink-pale: #fbd3e0;
    --green: #6ab023;
    --green-dark: #4f8f14;
    --white: #ffffff;
    --ink: #444444;
    --canvas: #f2f2f2;
  }
  * { box-sizing: border-box; margin: 0; padding: 0; }
  html, body { width: 1200px; height: 1000px; overflow: hidden; background: var(--canvas); }
  body { font-family: "Roboto Condensed", "Arial Narrow", sans-serif; position: relative; }

  .label {
    position: absolute; left: 10px; top: 288px; width: 1180px; height: 424px;
    border-radius: 22px; overflow: hidden; background: var(--white);
  }
  .label-waves { position: absolute; inset: 0; }

  .panel {
    position: absolute; top: 32px; width: 292px; height: 382px;
    background: rgba(255,255,255,0.78); border-radius: 14px;
    box-shadow: 0 0 6px rgba(0,0,0,0.12); padding: 12px 16px;
  }
  .panel-directions { left: 45px; }
  .panel-ingredients { left: 838px; }

  .panel-heading { color: var(--pink); font-weight: 700; font-size: 19px; line-height: 1; margin-bottom: 8px; }
  .directions-text { color: var(--green); font-size: 13px; line-height: 1.3; }
  .directions-warning { color: var(--pink); font-weight: 700; font-size: 13px; }

  .nutrition-box { border: 1.5px solid var(--pink); margin-top: 12px; padding: 8px 8px 6px; }
  .nutrition-title { color: var(--pink); font-weight: 700; font-size: 15px; text-align: center; margin-bottom: 8px; }
  .nutrition-note { color: var(--green); font-size: 11.5px; line-height: 1.3; }
  .nutrition-list { list-style: none; color: var(--pink); font-size: 11.5px; line-height: 1.3; margin-top: 8px; }
  .nutrition-key { display: flex; justify-content: space-between; font-size: 8px; color: var(--ink); margin-top: 3px; padding: 0 2px; }

  .marketing { color: var(--pink); font-size: 9.5px; line-height: 1.2; margin-top: 10px; font-style: italic; }
  .marketing strong { font-size: 12px; font-weight: 700; }
  .codes { color: var(--pink); font-weight: 700; font-size: 11.5px; line-height: 1.15; margin-top: 6px; }
  .contact { color: var(--pink); font-weight: 700; font-size: 8px; line-height: 1.35; margin-top: 3px; }

  .ingredients-text { color: var(--green); font-size: 12px; line-height: 1.25; }
  .tag {
    display: table; margin: 10px auto 0; background: var(--green); color: var(--white);
    font-weight: 700; font-size: 13px; padding: 2px 6px;
  }
  .tag-first { margin-top: 20px; }
  .suitable { color: var(--green); font-weight: 700; font-size: 14px; text-align: center; margin-top: 10px; }
  .advice {
    background: var(--pink); color: var(--white); font-weight: 700; font-size: 12.5px;
    text-align: center; line-height: 1.1; padding: 3px 6px; margin: 10px -16px 0;
  }
  .batch { position: absolute; left: 12px; bottom: 12px; color: var(--white); font-weight: 700; font-size: 14px; line-height: 1.1; }

  .brand { position: absolute; left: 350px; top: 26px; width: 500px; text-align: center; }
  .brand-name { display: inline-flex; align-items: center; gap: 6px; color: var(--pink); font-size: 32px; font-weight: 400; line-height: 1; }
  .brand-dot { width: 16px; height: 16px; border-radius: 50%; background: var(--pink); }
  .product-title {
    margin-top: 4px; font-weight: 900; font-size: 60px; line-height: 0.86; letter-spacing: 0.5px;
    background: linear-gradient(180deg, var(--pink-deep) 0%, var(--pink) 50%, #f06b93 100%);
    -webkit-background-clip: text; background-clip: text; color: transparent;
  }
  .capsule-count { color: var(--green); font-weight: 700; font-size: 20px; margin-top: 8px; }

  .fruit-art {
    position: absolute; left: 352px; top: 210px; width: 476px; height: 214px;
    background: radial-gradient(ellipse at 50% 25%, #4f9a2e 0%, #3a7d22 22%, rgba(230,40,85,0.95) 40%, #d8224f 70%, #b8173e 100%);
    border-radius: 60px 60px 0 0;
  }
  .food-supplement {
    position: absolute; left: 448px; top: 382px; width: 284px; height: 32px; border-radius: 16px;
    background: linear-gradient(180deg, #86c83a, var(--green-dark)); color: var(--white);
    font-weight: 700; font-size: 20px; text-align: center; line-height: 32px;
  }
</style>
</head>
<body>
  <section class="label">
    <svg class="label-waves" width="1180" height="424" viewBox="0 0 1180 424" aria-hidden="true">
      <rect x="0" y="0" width="1180" height="18" fill="var(--pink)"/>
      <path d="M0 260 C 220 230 360 300 520 340 C 700 385 920 330 1180 250 L1180 424 L0 424 Z" fill="var(--pink-pale)"/>
      <path d="M0 300 C 200 280 380 340 560 370 C 760 400 960 350 1180 300 L1180 424 L0 424 Z" fill="var(--pink-soft)"/>
      <path d="M0 360 C 240 350 420 390 600 405 C 820 420 1000 380 1180 350 L1180 424 L0 424 Z" fill="var(--pink)"/>
      <path d="M840 330 C 960 280 1080 230 1180 170 L1180 260 C 1080 300 960 330 840 340 Z" fill="var(--pink-soft)" opacity="0.7"/>
    </svg>

    <div class="panel panel-directions">
      <h2 class="panel-heading">DIRECTIONS:</h2>
      <p class="directions-text">Take 2 tablets/capsules per day with food.</p>
      <p class="directions-warning">Do not exceed the recommended intake</p>
      <div class="nutrition-box">
        <h3 class="nutrition-title">PRODUCT/ NUTRITION INFORMATION</h3>
        <p class="nutrition-note">Per tablet/capsule (min daily dose)<br>If daily dose is 2 tablets, the amount in 2 tablets must be listed.<br>If there is a RI then the percent of RI must be listed</p>
        <ul class="nutrition-list">
          <li>SEE CHECKLIST FOR DETAILS:</li>
          <li>300mg RASPBERRY KETONES EXTRACT 20%</li>
          <li>250mg ACAI BERRY EXTRACT 10:1</li>
          <li>200mg CAFFEINE Anhydrous</li>
          <li>250mg AFRICAN MANGO 36:1 EXTRACT</li>
        </ul>
      </div>
      <div class="nutrition-key"><span>RI = Reference Intake</span><span>|</span><span>* = No Reference Intake assessed</span></div>
      <p class="marketing"><strong>Marketting Text:</strong> Lorem ipsum dolor sit amet, consectetur adipiscing elit, sed do eiusmod tempor incididunt ut labore et dolore magna aliqua. Ut enim ad minim veniam, quis nostrud exercitation</p>
      <p class="codes">Product Code:<br>Label Code:</p>
      <p class="contact">Contact Number:<br>Address:<br>Email:</p>
    </div>

    <div class="brand">
      <div class="brand-name"><span class="brand-dot"></span>vorix</div>
      <h1 class="product-title">RASPBERRY<br>KETONE</h1>
      <p class="capsule-count">120 VEGETERIAN CAPSULES</p>
    </div>

    <div class="fruit-art" role="img" aria-label="Photograph of ripe red raspberries with green leaves"></div>
    <div class="food-supplement">FOOD SUPPLEMENT</div>

    <div class="panel panel-ingredients">
      <h2 class="panel-heading">INGREDIENTS:</h2>
      <p class="ingredients-text">In descending order of weight, including compound ingredients in brackets. Allergens must be identified as described in checklist.</p>
      <span class="tag tag-first">KEEP OUT OF REACH OF YOUNG CHILDREN</span>
      <span class="tag">STORE IN A COOL DRY PLACE</span>
      <p class="suitable">SUITABLE FOR VEGETARIANS &amp; VEGANS</p>
      <p class="advice">FOOD SUPPLEMENTS SHOULD NOT BE USED AS<br>A SUBSTITUTE FOR A VARIED DIET</p>
      <p class="batch">BATCH NUMBER:<br>BEST BEFORE END:</p>
    </div>
  </section>
</body>
</html>
```